Mix Comet business cards + chance to win packaging and other design projects

including logo already designed.

******** I need 2 business cards:
1. that is general for the company
2. that is specific for me

*********On the reverse side of the business card I want it to be divided into 4 boxes and each box to describe a stage in how to use the product. I need the boxes to be numbered and the contents to be easy to absorb and include graphics showing the actions also.
Turning then photo's into simplified, cool illustrations** would be really cool. This would allow changes, like writing "water" on the bottle etc etc. Maybe have a fftness lady drinking at the end? Imagination over to you.
The photo's are of the prototype so the illustrations can replace the grey caps with bright orange etc etc

CAPTIONS FOR ILLUSTRATIONS
1. Charge the Mix Comet
2.The Mix Comet is now ready for making a shake anywhere, anytime !
3. Choose any bottled water or beverage, release shot cap and Mix powder in.
4. Shake bottle, enjoy!
Updates

Can you illustrate?
I just changed the photos and captions to simplify.
Please re read the brief, thanks

Target Market(s)

Fitness, weight loss, health
male and female
any potential powdered drink user.

quince, skyroam design style ? Clean, simple, bold, clever, cool

Industry/Entity Type

Business

Requirements
Must have
• Must have logo and mixcomet.com

Card 1: email: info@mixcomet.com

Card 2: Rafe Dunmore LL.b. /President/ email:rafe@mixcomet.com/ office: 415 382 6619/ direct: 628 741 3085

I want the card to have a white background, not color blocked in.

I have included photos of the type of illustrations needed in each box.
In the illustrations pls make the mix comet army green and the caps bright orange.
Get the point across as simply as you can. Make it cool pls :)

```html
<!DOCTYPE html>
<html lang="en">
<head>
<meta charset="utf-8">
<title>Mix Comet Business Cards</title>
<link href="https://fonts.googleapis.com/css2?family=Oswald:wght@500;700&family=Roboto:wght@400;700&display=swap" rel="stylesheet">
<style>
  :root {
    --orange: #e8701f;
    --orange-dark: #d9601a;
    --orange-mid: #ee8237;
    --orange-light: #f39a55;
    --orange-pale: #f6b17a;
    --navy: #1d2a5c;
    --white: #ffffff;
    --bg: #ece8e2;
    --ink: #333;
    --art-green: #9aa77a;
    --art-skin: #f1d3b6;
  }
  * { box-sizing: border-box; margin: 0; padding: 0; }
  html, body { width: 1200px; height: 1000px; overflow: hidden; }
  body { background: var(--bg); position: relative; font-family: "Roboto", sans-serif; }

  .card {
    position: absolute; width: 540px; height: 290px;
    background: var(--white); border-radius: 16px; overflow: hidden;
    box-shadow: 0 4px 14px rgba(0,0,0,.18);
  }
  .card--steps { left: 60px; top: 30px; }
  .card--personal { left: 330px; top: 355px; }
  .card--general { left: 600px; top: 680px; }

  /* steps side */
  .steps { display: grid; grid-template-columns: repeat(4, 1fr); height: 100%; }
  .step { display: flex; flex-direction: column; min-width: 0; }
  .step__art {
    margin: 14px 10px 10px; height: 108px; border: 1.5px solid var(--orange);
    background: linear-gradient(160deg, var(--art-skin), var(--art-green));
  }
  .step__caption {
    flex: 1; padding: 0 10px; color: var(--orange);
    font-family: "Oswald", sans-serif; font-weight: 700; font-size: 15px; line-height: 1.1; text-transform: uppercase;
  }
  .step__caption small {
    display: block; font-family: "Roboto", sans-serif; font-weight: 400; text-transform: none;
    font-size: 10.5px; color: var(--ink); line-height: 1.25; margin: 2px 0;
  }
  .step__number {
    height: 58px; display: flex; align-items: center; justify-content: center;
    color: var(--white); font-family: "Oswald", sans-serif; font-weight: 700; font-size: 30px;
  }
  .step:nth-child(1) .step__number { background: var(--orange-dark); }
  .step:nth-child(2) .step__number { background: var(--orange-mid); }
  .step:nth-child(3) .step__number { background: var(--orange-light); }
  .step:nth-child(4) .step__number { background: var(--orange-pale); }

  /* front sides */
  .brand {
    position: absolute; display: flex; align-items: center; gap: 8px;
    font-family: "Oswald", sans-serif; font-weight: 700; color: var(--orange);
    text-transform: uppercase; letter-spacing: 1px; white-space: nowrap;
  }
  .brand__dot { width: 12px; height: 12px; border-radius: 50%; background: var(--orange); }
  .card--personal .brand { left: 34px; top: 150px; font-size: 40px; }
  .card--general .brand { left: 0; right: 0; top: 90px; justify-content: center; font-size: 50px; }

  .contact-band {
    position: absolute; left: 0; right: 0; bottom: 0; height: 44px;
    background: var(--orange); color: var(--white);
    display: flex; justify-content: space-between; align-items: center; padding: 0 22px;
    font-family: "Oswald", sans-serif; font-weight: 500; font-size: 14px; letter-spacing: .5px;
  }
  .contact-band span { display: flex; align-items: center; gap: 7px; }
  .contact-band svg { width: 14px; height: 14px; fill: var(--white); }

  .person { position: absolute; right: 30px; top: 30px; text-align: right; }
  .person__name { font-family: "Oswald", sans-serif; font-weight: 700; font-size: 21px; color: var(--navy); }
  .person__title { font-family: "Oswald", sans-serif; font-weight: 500; font-size: 14px; color: var(--orange); }
  .person__lines { margin-top: 34px; font-size: 12.5px; color: var(--navy); line-height: 1.7; }
  .person__lines div { display: flex; justify-content: flex-end; align-items: center; gap: 7px; }
  .person__lines svg { width: 11px; height: 11px; fill: var(--orange); }
</style>
</head>
<body>

<section class="card card--steps">
  <div class="steps">
    <div class="step">
      <div class="step__art" role="img" aria-label="Illustration: hands charging the green mixer with its orange cap"></div>
      <p class="step__caption">Charge the<br>Mix Comet</p>
      <div class="step__number">1</div>
    </div>
    <div class="step">
      <div class="step__art" role="img" aria-label="Illustration: hand holding the charged mixer"></div>
      <p class="step__caption">The Mix Comet<small>is now ready for making a shake anywhere, anytime!</small></p>
      <div class="step__number">2</div>
    </div>
    <div class="step">
      <div class="step__art" role="img" aria-label="Illustration: mixer fitted onto a water bottle"></div>
      <p class="step__caption"><small>Choose any bottled water or beverage, release shot cap and</small>Mix powder in.</p>
      <div class="step__number">3</div>
    </div>
    <div class="step">
      <div class="step__art" role="img" aria-label="Illustration: person drinking the shake"></div>
      <p class="step__caption">Shake bottle,<br>enjoy!</p>
      <div class="step__number">4</div>
    </div>
  </div>
</section>

<section class="card card--personal">
  <div class="brand"><span class="brand__dot"></span>Mix Comet</div>
  <div class="person">
    <div class="person__name">Rafe Dunmore LL.b.</div>
    <div class="person__title">President</div>
    <div class="person__lines">
      <div>415 382 6619 <svg viewBox="0 0 24 24"><path d="M6.6 10.8a15 15 0 0 0 6.6 6.6l2.2-2.2c.3-.3.7-.4 1-.2 1.1.4 2.3.6 3.6.6.6 0 1 .4 1 1V20c0 .6-.4 1-1 1A17 17 0 0 1 3 4c0-.6.4-1 1-1h3.5c.6 0 1 .4 1 1 0 1.3.2 2.5.6 3.6.1.3 0 .7-.2 1z"/></svg></div>
      <div>628 741 3085 <svg viewBox="0 0 24 24"><rect x="6" y="2" width="12" height="20" rx="2"/></svg></div>
      <div>rafe@mixcomet.com <svg viewBox="0 0 24 24"><path d="M2 5h20v14H2zm2 2v.5l8 5 8-5V7z"/></svg></div>
    </div>
  </div>
  <div class="contact-band">
    <span><svg viewBox="0 0 24 24"><circle cx="12" cy="12" r="10"/></svg>WWW.MIXCOMET.COM</span>
    <span><svg viewBox="0 0 24 24"><path d="M2 5h20v14H2zm2 2v.5l8 5 8-5V7z"/></svg>INFO@MIXCOMET.COM</span>
  </div>
</section>

<section class="card card--general">
  <div class="brand"><span class="brand__dot"></span>Mix Comet</div>
  <div class="contact-band">
    <span><svg viewBox="0 0 24 24"><circle cx="12" cy="12" r="10"/></svg>WWW.MIXCOMET.COM</span>
    <span><svg viewBox="0 0 24 24"><path d="M2 5h20v14H2zm2 2v.5l8 5 8-5V7z"/></svg>INFO@MIXCOMET.COM</span>
  </div>
</section>

</body>
</html>
```